Laptop Accessories Packing Design

We are looking for a new package design of a laptop accesories (batteries, charges, hard drives etc.). We want to refresh our brand Velmora GridWorks. At VelmoraGrid, we create high-end laptop accessories that ensure reliability, performance, and longevity for users worldwide. Our mission is to deliver innovative and durable solutions that allow users to work, create, and grow without limits.
General Packaging Concept
Minimalist and elegant look, yet with elements that catch the eye (Velmora products will mainly be offered on auction portals such as Trivana, Zubo, Kestrix, so it would be good if the packaging attracted attention and stood out from the competitors).
Should I put a photo, sketch or product icon on the box? We'll leave that to your imagination.
We ask for a general design of the packaging. After the competition, together with the winner, we will add the rest of the information to the back and sides of the box.
In the attachments there is our Logo (you can use other colors) and sample packaging of competitors
Target Market(s)
E-commerse
Industry/Entity Type
individual end customer
Look and feel
Each slider illustrates characteristics of the customer's brand and the style your logo design should communicate.

```html
<!DOCTYPE html>
<html lang="en">
<head>
<meta charset="utf-8">
<title>Velmora GridWorks – Laptop Accessories Box Dieline</title>
<link rel="stylesheet" href="https://fonts.googleapis.com/css2?family=Exo+2:ital,wght@0,700;0,800;1,400;1,500&family=Poppins:wght@400;600;700&family=Barlow+Condensed:wght@400;500&display=swap">
<style>
  :root {
    --carbon: #1b1b1b;
    --carbon-deep: #111111;
    --copper-dark: #a9491a;
    --copper-mid: #d6743a;
    --copper-light: #f6ad70;
    --accent: #e98a3e;
    --ink: #161616;
    --white: #ffffff;
    --cut: #c62828;
    --page: #ffffff;
  }
  html, body { margin: 0; padding: 0; overflow: hidden; background: var(--page); }
  .dieline { position: relative; width: 1200px; height: 355px; overflow: hidden; background: var(--page); }
  .dieline svg.shapes { position: absolute; inset: 0; }
  .label { position: absolute; margin: 0; white-space: nowrap; }

  .brand-name { font-family: "Exo 2", sans-serif; font-weight: 800; color: var(--ink); letter-spacing: -0.5px; line-height: 1; }
  .lid-brand { left: 286px; top: 74px; font-size: 30px; transform: translate(-50%, -50%) rotate(180deg); }
  .front-brand { left: 315px; top: 146px; font-size: 34px; transform: translate(-50%, -50%); }
  .side-brand { left: 573px; top: 197px; font-size: 30px; color: var(--white); transform: translate(-50%, -50%) rotate(-90deg); }

  .product-title { left: 240px; top: 193px; font-family: "Exo 2", sans-serif; font-style: italic; font-weight: 500; font-size: 25px; line-height: 24px; }
  .product-title .line-accent { color: var(--accent); display: block; }
  .product-title .line-main { color: var(--white); display: block; }
  .product-tagline { left: 240px; top: 248px; font-family: "Poppins", sans-serif; font-size: 5.4px; letter-spacing: 0.5px; color: #cfcfcf; }
  .product-tagline strong { color: var(--white); font-weight: 600; }

  .back-copy { left: 862px; top: 129px; width: 430px; transform: translateX(-50%); white-space: normal; text-align: center; font-family: "Poppins", sans-serif; font-weight: 600; font-size: 9.2px; line-height: 13px; color: var(--ink); }

  .feature { position: absolute; top: 203px; width: 50px; margin-left: -25px; text-align: center; }
  .feature-label { display: block; margin-top: 4px; font-family: "Barlow Condensed", sans-serif; font-size: 9.5px; color: var(--white); }
  .maker-title { left: 782px; top: 208px; font-family: "Poppins", sans-serif; font-weight: 700; font-size: 8.6px; color: var(--white); }
  .maker-site { left: 781px; top: 221px; font-family: "Poppins", sans-serif; font-size: 18px; color: var(--white); }

  .side-title { left: 1133px; top: 201px; transform: translate(-50%, -50%) rotate(-90deg); font-family: "Exo 2", sans-serif; font-style: italic; font-size: 12.5px; }
  .side-title .accent { color: var(--accent); }
  .side-title .main { color: var(--white); }
  .side-specs { left: 1171px; top: 201px; transform: translate(-50%, -50%) rotate(-90deg); font-family: "Barlow Condensed", sans-serif; font-size: 11px; color: var(--white); letter-spacing: 0.3px; }
</style>
</head>
<body>
<main class="dieline">
  <svg class="shapes" width="1200" height="355" viewBox="0 0 1200 355" aria-hidden="true">
    <defs>
      <linearGradient id="copper" x1="0" x2="1" y1="0" y2="0">
        <stop offset="0" stop-color="var(--copper-dark)"/>
        <stop offset="0.45" stop-color="var(--copper-light)"/>
        <stop offset="1" stop-color="var(--copper-dark)"/>
      </linearGradient>
    </defs>
    <g class="carbon-panels" fill="var(--carbon)">
      <!-- lid tuck flap -->
      <path d="M37 34 V22 Q37 5 60 5 H510 Q532 5 532 22 V34 Z"/>
      <!-- left glue side -->
      <path d="M16 122 L37 113 V272 L16 260 Z"/>
      <!-- front panel dark -->
      <rect x="37" y="182" width="497" height="90"/>
      <!-- front bottom flap -->
      <path d="M37 272 H534 L408 310 V340 Q408 352 392 352 H176 Q161 352 161 340 V310 Z"/>
      <!-- side panel -->
      <rect x="535" y="113" width="78" height="159"/>
      <path d="M541 58 H597 L609 113 H537 Z"/>
      <path d="M535 272 H613 L600 352 H535 V340 Q590 340 575 322 L573 320 Z"/>
      <!-- back panel dark -->
      <rect x="613" y="182" width="498" height="90"/>
      <path d="M613 272 H1111 L1095 352 H1005 L986 312 H738 L719 352 H625 Z"/>
      <!-- right side panel -->
      <rect x="1111" y="113" width="80" height="159"/>
      <path d="M1120 58 H1183 L1187 113 H1115 Z"/>
      <path d="M1111 272 H1191 V352 H1150 L1150 340 Q1140 330 1152 322 Z"/>
    </g>
    <g class="copper-bands">
      <rect x="37" y="34" width="497" height="77" fill="url(#copper)"/>
      <rect x="37" y="111" width="497" height="71" fill="url(#copper)"/>
      <rect x="613" y="113" width="498" height="69" fill="url(#copper)"/>
    </g>
    <g class="fold-lines" stroke="var(--cut)" stroke-width="0.5" fill="none">
      <line x1="37" y1="34" x2="534" y2="34"/>
      <line x1="37" y1="111" x2="534" y2="111"/>
      <line x1="37" y1="272" x2="1191" y2="272"/>
      <line x1="534" y1="113" x2="1191" y2="113"/>
      <line x1="534.5" y1="111" x2="534.5" y2="272"/>
      <line x1="613" y1="113" x2="613" y2="272"/>
      <line x1="1111" y1="113" x2="1111" y2="272"/>
    </g>
    <rect class="product-illustration" role="img" aria-label="Line illustration of an open laptop" x="63" y="131" width="160" height="118" rx="6" fill="#2a2a2a" stroke="#5a5a5a" stroke-width="0.6"/>
    <g class="feature-icons" fill="var(--carbon-deep)" stroke="var(--accent)" stroke-width="1.6">
      <circle cx="660" cy="216" r="14"/>
      <circle cx="704" cy="216" r="14"/>
      <circle cx="748" cy="216" r="14"/>
    </g>
    <g class="feature-glyphs" fill="var(--accent)">
      <path d="M655 216 l4 4 l7 -8" stroke="var(--accent)" stroke-width="2" fill="none"/>
      <path d="M696 220 a8 8 0 0 1 16 0" stroke="var(--accent)" stroke-width="2" fill="none"/>
      <line x1="704" y1="220" x2="708" y2="213" stroke="var(--accent)" stroke-width="1.6"/>
      <rect x="744" y="207" width="8" height="16" rx="1.5"/>
    </g>
    <g class="connectivity-icons" stroke="var(--white)" stroke-width="1.3" fill="none">
      <path d="M1146 258 a6 6 0 0 1 0 -10 M1142 261 a10 10 0 0 1 0 -16"/>
      <circle cx="1151" cy="253" r="1.4" fill="var(--white)"/>
      <path d="M1146 202 l10 8 l-5 4 v-16 l5 4 l-10 8"/>
      <path d="M1151 150 v14 M1147 164 l4 -10 l4 10"/>
      <circle cx="1151" cy="150" r="2.5"/>
    </g>
  </svg>

  <p class="label brand-name lid-brand">Velmora</p>
  <p class="label brand-name front-brand">Velmora</p>
  <h1 class="label product-title"><span class="line-accent">LAPTOP</span><span class="line-main">ACCESSORIES</span></h1>
  <p class="label product-tagline">HIGH-END LAPTOP <strong>BATTERIES, CHARGES, HARD DRIVES</strong></p>

  <p class="label brand-name side-brand">Velmora</p>

  <p class="label back-copy">Lorem Ipsum is simply dummy text of the printing and typesetting industry. Lorem Ipsum has been the industry's standard dummy text ever since the 1500s, when an unknown printer took a galley of type and scrambled it to make a type specimen book.</p>
  <div class="feature" style="left:660px"><span class="feature-label" style="margin-top:29px">Reliability</span></div>
  <div class="feature" style="left:704px"><span class="feature-label" style="margin-top:29px">Performance</span></div>
  <div class="feature" style="left:748px"><span class="feature-label" style="margin-top:29px">Longevity</span></div>
  <p class="label maker-title">Manufactured and Manufactured by:</p>
  <p class="label maker-site">yourwebsite.com</p>

  <p class="label side-title"><span class="accent">LAPTOP</span> <span class="main">ACCESSORIES</span></p>
  <p class="label side-specs">Wifi &nbsp;|&nbsp; Bluetooth &nbsp;|&nbsp; 4G/5G</p>
</main>
</body>
</html>
```